Business Card Design Project

Looking to update our business cards. We have a logo with our slogan. We are an IT firm so we wouldlike a modern look.

Industry/Entity Type

Business

```html
<!DOCTYPE html>
<html lang="en">
<head>
<meta charset="UTF-8">
<title>Novaline Inc – Business Card</title>
<link rel="stylesheet" href="https://fonts.googleapis.com/css2?family=Cinzel:wght@400;700;800&display=swap">
<style>
  :root {
    --backdrop: #000000;
    --card-white: #ffffff;
    --card-black: #000000;
    --accent-green: #4f9a12;
    --logo-green: #5e9e1f;
    --ink: #111111;
    --label-white: #ffffff;
  }
  * { margin: 0; padding: 0; box-sizing: border-box; }
  html, body {
    width: 1149px;
    height: 1200px;
    overflow: hidden;
    background: var(--backdrop);
  }
  .canvas {
    position: relative;
    width: 1149px;
    height: 1200px;
    background: var(--backdrop);
    font-family: "Cinzel", serif;
  }
  .side-label {
    position: absolute;
    color: var(--label-white);
    font-weight: 700;
    font-size: 58px;
    line-height: 1;
    letter-spacing: 1px;
  }
  .side-label--front { left: 855px; top: 268px; }
  .side-label--back { left: 134px; top: 828px; }

  .card {
    position: absolute;
    background: var(--card-white);
  }
  .card--front { left: 112px; top: 105px; width: 703px; height: 488px; }
  .card--back { left: 361px; top: 627px; width: 707px; height: 480px; }

  .card__trim {
    position: absolute;
    left: 0; top: 0;
    width: 100%; height: 100%;
    overflow: visible;
  }
  .card__trim line {
    stroke: var(--accent-green);
    stroke-width: 4;
  }

  .front__panel {
    position: absolute;
    left: 49px; top: 58px;
    width: 614px; height: 373px;
    background: var(--card-black);
    display: flex;
    align-items: center;
    justify-content: center;
  }
  .brand-name {
    color: var(--logo-green);
    font-weight: 700;
    font-size: 64px;
    letter-spacing: 4px;
    line-height: 1;
  }

  .back__identity {
    position: absolute;
    left: 0; top: 155px;
    width: 100%;
    text-align: center;
    color: var(--ink);
  }
  .back__name {
    font-weight: 800;
    font-size: 42px;
    line-height: 1;
    letter-spacing: 0.5px;
  }
  .back__position {
    margin-top: 10px;
    font-weight: 700;
    font-size: 30px;
    line-height: 1;
  }
  .contact {
    position: absolute;
    color: var(--ink);
    font-size: 13px;
    line-height: 20px;
    font-family: "Cinzel", serif;
  }
  .contact__label { font-weight: 700; }
  .contact__value {
    font-family: "Arial", sans-serif;
    font-size: 13px;
  }
  .contact--web { left: 80px; top: 301px; }
  .contact--phone { left: 488px; top: 315px; }
</style>
</head>
<body>
<main class="canvas">

  <section class="card card--front" aria-label="Card front">
    <svg class="card__trim" viewBox="0 0 703 488" aria-hidden="true">
      <line x1="10" y1="17" x2="10" y2="84"/>
      <line x1="8" y1="17" x2="55" y2="17"/>
      <line x1="87" y1="17" x2="672" y2="17"/>
      <line x1="691" y1="407" x2="691" y2="472"/>
      <line x1="647" y1="472" x2="693" y2="472"/>
      <line x1="15" y1="472" x2="621" y2="472"/>
    </svg>
    <div class="front__panel">
      <span class="brand-name">NOVALINE INC</span>
    </div>
  </section>

  <div class="side-label side-label--front">Front</div>
  <div class="side-label side-label--back">Back</div>

  <section class="card card--back" aria-label="Card back">
    <svg class="card__trim" viewBox="0 0 707 480" aria-hidden="true">
      <line x1="14" y1="16" x2="14" y2="80"/>
      <line x1="12" y1="16" x2="60" y2="16"/>
      <line x1="92" y1="15" x2="645" y2="15"/>
      <line x1="697" y1="401" x2="697" y2="467"/>
      <line x1="652" y1="467" x2="699" y2="467"/>
      <line x1="70" y1="466" x2="626" y2="466"/>
    </svg>
    <div class="back__identity">
      <div class="back__name">YOUR NAME HERE</div>
      <div class="back__position">YOUR POSITION</div>
    </div>
    <div class="contact contact--web">
      <div><span class="contact__label">Email :</span> <span class="contact__value">yourname@xxx.com</span></div>
      <div><span class="contact__label">Web</span> <span class="contact__value">: www.websitename.com</span></div>
    </div>
    <div class="contact contact--phone">
      <div><span class="contact__label">Phone :</span> <span class="contact__value">00-11-222-3333</span></div>
      <div><span class="contact__label">Fax:</span> <span class="contact__value">00-11-222-3333</span></div>
    </div>
  </section>

</main>
</body>
</html>
```